Keelby marketing postcards (6x9)

I would like to replicate this 6x9 postcard, but update name/logo, phone number, web address, etc. I also need to create a second postcard copying this basic design, but with updated content and background pictures. Updated contact info to be used for both postcards:
Website: www.keelbyhomestay.com
Name: Mark Tessler
Email: mtessler@keelbyhomestay.com
Phone: (555) 246-8130

Requirements
Must have
• Need two 6x9 postcard designs; 1 themed for Rivenport College, 1 for Calder State. Have uploaded photos that can be used in design. RC can be used for RC postcard (only), CS can be used for CS (only), Generic can be used for either. I've tried to upload extra photos so that you can use your creativity in selecting those that work best in the design.
Nice to have
• In the "Color palette" file, it has the two color schemes -- one for Rivenport College and one for Calder State. Those respective color schemes should be heavily represented in each design. Then there are different groups of pictures labelled either "CS" or "RC", plus some labelled "Generic". The generic ones can be used in either design, the others should be used only for the design for that school.

```html
<!DOCTYPE html>
<html lang="en">
<head>
<meta charset="utf-8">
<title>Keelby Homestay Postcard</title>
<link rel="stylesheet" href="https://fonts.googleapis.com/css2?family=Open+Sans:wght@400;600;700&family=Ubuntu:wght@500;700&display=swap">
<style>
  :root{
    --stage:#0b0d0f;
    --navy:#1c1d42;
    --navy-deep:#101128;
    --mint:#7ff5d6;
    --mint-text:#5fe8c8;
    --blue:#4a63ee;
    --ink:#3a3d48;
    --white:#ffffff;
    --line:#b9c6c2;
    --stamp:#e7ecea;
    --skyline:#a9b3b5;
  }
  *{box-sizing:border-box;margin:0;padding:0}
  html,body{width:1200px;height:800px;overflow:hidden;background:var(--stage)}
  body{position:relative;font-family:"Open Sans",sans-serif}
  .postcard{position:absolute;top:213px;width:560px;height:373px;background:var(--white);overflow:hidden}
  .postcard--front{left:27px}
  .postcard--back{left:613px}
  .postcard svg.art{position:absolute;inset:0}
  .brand{position:absolute;font-family:"Open Sans",sans-serif;font-weight:700;font-size:13px;color:var(--blue);letter-spacing:.5px;display:flex;align-items:center;gap:6px}
  .brand__dot{width:9px;height:9px;border-radius:50%;background:var(--mint-text)}
  /* front */
  .front__eyebrow{position:absolute;left:40px;top:86px;color:var(--white);font-size:12px;display:flex;align-items:center;gap:8px}
  .front__flag{width:24px;height:15px;background:linear-gradient(#c43a3a 50%,#2b3d8f 50%);border-radius:2px}
  .front__headline{position:absolute;left:40px;top:106px;font-family:"Ubuntu",sans-serif;font-weight:700;font-size:26px;line-height:27px;text-transform:uppercase;color:var(--white)}
  .front__headline .accent{color:var(--mint-text)}
  .front__rule{position:absolute;left:40px;top:218px;width:238px;height:1px;background:rgba(255,255,255,.6)}
  .front__copy{position:absolute;left:40px;top:228px;width:230px;color:var(--white);font-size:11px;line-height:15px}
  .front__years{position:absolute;left:40px;top:262px;font-family:"Ubuntu",sans-serif;font-weight:500;font-size:18px;color:var(--mint-text)}
  /* back */
  .back__copy{position:absolute;left:128px;top:44px;width:166px;font-size:9.5px;line-height:13px;color:var(--ink)}
  .back__copy p{margin-bottom:8px}
  .back__cta{position:absolute;left:210px;top:196px;font-family:"Ubuntu",sans-serif;font-weight:700;font-size:17px;line-height:18px;color:var(--blue);text-transform:uppercase}
  .back__contact{position:absolute;left:20px;top:286px;color:var(--white)}
  .back__name{font-family:"Ubuntu",sans-serif;font-weight:500;font-size:15px;margin-bottom:6px}
  .back__row{display:flex;align-items:center;gap:6px;font-size:9.5px;line-height:13px}
  .back__row svg{width:9px;height:9px;flex:none}
</style>
</head>
<body>

<section class="postcard postcard--front">
  <svg class="art" viewBox="0 0 560 373">
    <defs>
      <linearGradient id="capitolPhoto" x1="0" y1="0" x2="0" y2="1">
        <stop offset="0" stop-color="#3f9ad8"/>
        <stop offset=".45" stop-color="#6f9c86"/>
        <stop offset="1" stop-color="#3e7a2c"/>
      </linearGradient>
      <linearGradient id="towerPhoto" x1="0" y1="0" x2="0" y2="1">
        <stop offset="0" stop-color="#8fbfe8"/>
        <stop offset=".6" stop-color="#e6ddd0"/>
        <stop offset="1" stop-color="#4f7d3a"/>
      </linearGradient>
      <linearGradient id="nightPanel" x1="0" y1="0" x2="0" y2="1">
        <stop offset="0" stop-color="var(--navy)"/>
        <stop offset="1" stop-color="var(--navy-deep)"/>
      </linearGradient>
    </defs>
    <path role="img" aria-label="Photo of the state capitol dome among green trees" d="M0 0H560V190Q500 295 330 310H0Z" fill="url(#capitolPhoto)"/>
    <circle cx="110" cy="68" r="245" fill="url(#nightPanel)" stroke="var(--white)" stroke-width="6"/>
    <circle role="img" aria-label="Photo of Rivenport College bell tower" cx="435" cy="212" r="62" fill="url(#towerPhoto)" stroke="var(--white)" stroke-width="5"/>
    <circle cx="286" cy="218" r="4" fill="none" stroke="var(--white)" stroke-width="1"/>
  </svg>
  <div class="front__eyebrow"><span>Calder State Families</span><span class="front__flag" role="img" aria-label="State flag graphic"></span></div>
  <h1 class="front__headline">Let us help<br><span class="accent">you save<br>thousands on</span><br>tuition costs</h1>
  <div class="front__rule"></div>
  <p class="front__copy">We have been helping out-of state families gain texas residency for over</p>
  <p class="front__years">14 YEARS.</p>
  <div class="brand" style="left:40px;top:338px"><span class="brand__dot"></span>KEELBY HOMESTAY</div>
</section>

<section class="postcard postcard--back">
  <svg class="art" viewBox="0 0 560 373">
    <path d="M0 120Q130 150 190 250Q225 320 262 373H0Z" fill="var(--mint)"/>
    <circle role="img" aria-label="Photo of a student carrying books" cx="70" cy="150" r="50" fill="#9bb5d0" stroke="var(--white)" stroke-width="5"/>
    <circle role="img" aria-label="Photo of the clock tower lit at night" cx="155" cy="255" r="44" fill="#6a1e24" stroke="var(--white)" stroke-width="5"/>
    <path role="img" aria-label="Photo of the Calder Campus water tower with flowering tree" d="M262 373Q235 320 250 285Q285 255 330 270Q350 320 335 373Z" fill="#b39ac0"/>
    <rect role="img" aria-label="Grey city skyline illustration" x="330" y="250" width="230" height="123" fill="var(--skyline)" opacity=".7"/>
    <line x1="300" y1="35" x2="300" y2="245" stroke="var(--line)" stroke-width="1.2" stroke-dasharray="9 7"/>
    <rect x="470" y="22" width="70" height="70" rx="4" fill="var(--stamp)"/>
    <g stroke="var(--line)" stroke-width="1">
      <line x1="335" y1="120" x2="540" y2="120"/>
      <line x1="335" y1="148" x2="540" y2="148"/>
      <line x1="335" y1="176" x2="540" y2="176"/>
      <line x1="335" y1="204" x2="540" y2="204"/>
    </g>
  </svg>
  <div class="brand" style="left:322px;top:62px"><span class="brand__dot"></span>KEELBY HOMESTAY</div>
  <div class="back__copy">
    <p>Calder parents,did you know you can save over $13,800 a semester in tuition?</p>
    <p>Establishing Texas residency through a property purchase is as easy as 1-2-3.</p>
    <p>Contact us to learn how we have helped more than 500 families- and counting-save thousands on tution.</p>
  </div>
  <p class="back__cta">Let us<br>help you<br>too.</p>
  <div class="back__contact">
    <p class="back__name">Mark Tessler</p>
    <p class="back__row"><svg viewBox="0 0 10 10"><path d="M2 1h2l1 2-1 1a5 5 0 0 0 2 2l1-1 2 1v2a1 1 0 0 1-1 1A8 8 0 0 1 1 2a1 1 0 0 1 1-1z" fill="currentColor"/></svg>(555) 246-8130</p>
    <p class="back__row"><svg viewBox="0 0 10 10"><circle cx="5" cy="5" r="4" fill="none" stroke="currentColor"/><path d="M1 5h8M5 1v8" stroke="currentColor" stroke-width=".8"/></svg>www.keelbyhomestay.com</p>
    <p class="back__row"><svg viewBox="0 0 10 10"><rect x="1" y="2" width="8" height="6" fill="none" stroke="currentColor"/><path d="M1 2l4 3 4-3" fill="none" stroke="currentColor"/></svg>mtessler@keelbyhomestay.com</p>
  </div>
</section>

</body>
</html>
```